Wine Label for a White and a Red Wine from Italy

We have a very good idea of what we want with artwork. We need you to please design a 'template' with the text so we can change out the artwork from year to year. Samples are shown of what we are looking for. We are looking for options with the two basic designs. Brand name of wine is: Valora di Castegno. Both wines are in a light green Bordeaux-style bottle (note: we don't show a light green bottle in the mockup but please remember the bottle is light green). Artwork is provided. We'd like to see either the green or blue butterfly on the white wine, the red butterfly is for the red wine. Please base the design on the attached label from Brailey and/or the attached label from Chateau Mervanges.

Target Market(s)

Millennials, women

Requirements
Must have
• The artwork (butterflies) attached.
Nice to have
• Elegant, readable fonts. Please make the text so it can be changed by the printer. Please make it so the artwork can be changed too.

```html
<!DOCTYPE html>
<html lang="en">
<head>
<meta charset="utf-8">
<title>Valora di Castegno – Barrel Select Labels</title>
<link href="https://fonts.googleapis.com/css2?family=Cormorant+Garamond:wght@500&family=Montserrat:wght@300;400;600&display=swap" rel="stylesheet">
<style>
  :root {
    --canvas: #ffffff;
    --label-paper: #efede6;
    --ink: #111111;
    --select-green: #1a6b3c;
    --select-red: #c0202f;
    --white-art-light: #fbf8ee;
    --white-art-mid: #a9b879;
    --white-art-dark: #44583a;
    --red-art-light: #f4b73a;
    --red-art-mid: #e39a16;
    --red-art-teal: #1d8c94;
  }
  html, body {
    margin: 0;
    padding: 0;
    width: 1200px;
    height: 1200px;
    overflow: hidden;
    background: var(--canvas);
  }
  .canvas {
    position: relative;
    width: 1200px;
    height: 1200px;
  }
  .label {
    position: absolute;
    top: 354px;
    width: 370px;
    height: 516px;
  }
  .label--white { left: 209px; }
  .label--red { left: 628px; }
  .label svg { display: block; width: 370px; height: 516px; }
  .paper { fill: var(--label-paper); }
  .brand-name {
    font-family: "Cormorant Garamond", serif;
    font-weight: 500;
    font-size: 42px;
    letter-spacing: 0.06em;
    fill: var(--ink);
  }
  .brand-sub {
    font-family: "Cormorant Garamond", serif;
    font-weight: 500;
    font-size: 23px;
    fill: var(--ink);
  }
  .cuvee {
    font-family: "Montserrat", sans-serif;
    font-weight: 600;
    font-size: 21px;
    letter-spacing: 0.12em;
  }
  .label--white .cuvee { fill: var(--select-green); }
  .label--red .cuvee { fill: var(--select-red); }
  .vintage {
    font-family: "Montserrat", sans-serif;
    font-weight: 600;
    font-size: 21px;
    letter-spacing: 0.18em;
    fill: var(--ink);
  }
  .wine-type {
    font-family: "Montserrat", sans-serif;
    font-weight: 600;
    font-size: 17px;
    letter-spacing: 0.2em;
    fill: var(--ink);
  }
  .origin {
    font-family: "Montserrat", sans-serif;
    font-weight: 300;
    font-size: 13.5px;
    letter-spacing: 0.1em;
    fill: var(--ink);
  }
  .maker, .farming {
    font-family: "Montserrat", sans-serif;
    font-weight: 300;
    font-size: 10px;
    letter-spacing: 0.12em;
    fill: var(--ink);
  }
</style>
</head>
<body>
<main class="canvas">

  <section class="label label--white" aria-label="Valora di Castegno Barrel Select white wine label">
    <svg viewBox="0 0 370 516" xmlns="http://www.w3.org/2000/svg">
      <defs>
        <radialGradient id="artwork-white" cx="0.48" cy="0.5" r="0.6">
          <stop offset="0" stop-color="var(--white-art-dark)"/>
          <stop offset="0.35" stop-color="var(--white-art-mid)"/>
          <stop offset="0.75" stop-color="var(--white-art-light)"/>
          <stop offset="1" stop-color="#ffffff"/>
        </radialGradient>
      </defs>
      <polygon class="paper" points="0,0 370,0 366,142 5,142"/>
      <rect x="5" y="142" width="361" height="223" fill="url(#artwork-white)" role="img" aria-label="Artwork: painted green butterfly on a soft white ground"/>
      <polygon class="paper" points="12,365 357,365 353,516 16,516"/>
      <text class="brand-name" x="185" y="62" text-anchor="middle">VALORA</text>
      <text class="brand-sub" x="185" y="88" text-anchor="middle">di Castegno</text>
      <text class="cuvee" x="185" y="128" text-anchor="middle">BARREL SELECT</text>
      <text class="vintage" x="185" y="399" text-anchor="middle">2018</text>
      <text class="wine-type" x="185" y="428" text-anchor="middle">BIANCO</text>
      <text class="origin" x="185" y="452" text-anchor="middle">Piemonte Italy</text>
      <text class="maker" x="185" y="474" text-anchor="middle">Artisanlly Crafted by Cantina Vallerossa</text>
      <text class="farming" x="185" y="497" text-anchor="middle">sustainably farmed</text>
    </svg>
  </section>

  <section class="label label--red" aria-label="Valora di Castegno Barrel Select label, red butterfly version">
    <svg viewBox="0 0 370 516" xmlns="http://www.w3.org/2000/svg">
      <defs>
        <radialGradient id="artwork-red" cx="0.5" cy="0.45" r="0.65">
          <stop offset="0" stop-color="var(--red-art-teal)"/>
          <stop offset="0.3" stop-color="#1e3b3c"/>
          <stop offset="0.5" stop-color="var(--red-art-mid)"/>
          <stop offset="1" stop-color="var(--red-art-light)"/>
        </radialGradient>
      </defs>
      <polygon class="paper" points="0,0 370,0 366,142 5,142"/>
      <rect x="5" y="142" width="361" height="223" fill="url(#artwork-red)" role="img" aria-label="Artwork: painted teal and black butterfly on a golden orange ground"/>
      <polygon class="paper" points="12,365 357,365 353,516 16,516"/>
      <text class="brand-name" x="185" y="62" text-anchor="middle">VALORA</text>
      <text class="brand-sub" x="185" y="88" text-anchor="middle">di Castegno</text>
      <text class="cuvee" x="185" y="128" text-anchor="middle">BARREL SELECT</text>
      <text class="vintage" x="185" y="399" text-anchor="middle">2018</text>
      <text class="wine-type" x="185" y="428" text-anchor="middle">BIANCO</text>
      <text class="origin" x="185" y="452" text-anchor="middle">Piemonte Italy</text>
      <text class="maker" x="185" y="474" text-anchor="middle">Artisanlly Crafted by Cantina Vallerossa</text>
      <text class="farming" x="185" y="497" text-anchor="middle">sustainably farmed</text>
    </svg>
  </section>

</main>
</body>
</html>
```